Website For Custom Home Builder

-Very elegant and simple design as I am a high end custom home builder.
-I build homes $2 million to $10 million range so the website needs to reflect the level of home that I build.
-Attached are photos of homes I have built to use as well as my logo.
-I need final design to be in layered format so my local guy can edit if he needs to.

3 Page Design
1. HomePage:
-logo, some photos,
-“Building beautiful custom homes in Indianapolis for over 20 years”
2. AboutPage:
-Wade Holloran has been building stunning custom homes in the Indianpolis area for over 20 years. As a small boutique building company we only build a handful of homes a year in order to offer our clients the personal attention that their homes deserve. It's this attention to detail that makes our client experience and final product something special and unique.
- family photo
3. ContactPage:
-office photo
-317-552-7190
-wade@whcrafted.com
-415 North Fernmill Rd, Suite 308, Carmel IN 46033

Target Market(s)

Very high end clients looking to build $2 million to $10 million homes.

Industry/Entity Type

Residential high end custom home builder/construction

Coding

Coded - Design and coding required

Number of Pages Required

3 page

Requirements
Must have
• Very simple and elegant design that represents the high end homes that I build.
Nice to have
Should not have
• Should NOT have a lot of clutter or be a very busy page from a design perspective.

```html
<!DOCTYPE html>
<html lang="en">
<head>
<meta charset="utf-8">
<title>Wade Holloran Custom Homes</title>
<link href="https://fonts.googleapis.com/css2?family=Poppins:wght@300;400;500;600&display=swap" rel="stylesheet">
<style>
:root{
  --accent:#c8622f;
  --accent-line:#d98a2b;
  --ink:#1d1a17;
  --white:#ffffff;
  --sky-top:#b8a48a;
  --sky-glow:#d8894a;
  --house:#5a3c26;
  --lawn:#3f4a22;
  --footer-top:#b4562a;
  --footer-bottom:#4e2412;
  --panel:rgba(110,100,92,.62);
}
*{margin:0;padding:0;box-sizing:border-box}
html,body{width:1200px;height:1171px;overflow:hidden;background:var(--white)}
body{font-family:'Poppins',sans-serif;position:relative}
.site{position:absolute;left:285px;top:0;width:703px;height:1171px;overflow:hidden}
.section{position:absolute;left:0;width:703px;overflow:hidden}
.photo{position:absolute;inset:0}
.photo-front{background:
  linear-gradient(180deg,rgba(0,0,0,0) 0%,rgba(0,0,0,.15) 100%),
  radial-gradient(ellipse at 40% 25%,#e59a55 0%,rgba(229,154,85,0) 55%),
  linear-gradient(180deg,var(--sky-top) 0%,var(--sky-glow) 28%,#8a5a3a 45%,var(--house) 70%,#6b5236 86%,var(--lawn) 92%,#51602b 100%)}
.photo-back{background:
  radial-gradient(ellipse at 50% 58%,#f0a640 0%,rgba(240,166,64,0) 45%),
  linear-gradient(180deg,#c79a72 0%,#d68a4c 15%,#6a4428 40%,#7a4f2a 62%,#8a7a68 78%,#4c5a28 100%)}
.photo-contact{background:
  linear-gradient(180deg,#b59d83 0%,#a88a70 30%,#7e6652 60%,#5b4a38 85%,#3f4a22 100%)}
.hero{top:0;height:328px}
.about{top:328px;height:363px}
.contact{top:691px;height:368px}

.header{position:absolute;left:0;top:0;width:703px;height:50px}
.brand{position:absolute;left:34px;top:26px;font-size:11.5px;font-weight:500;color:var(--ink);letter-spacing:.2px;display:flex;align-items:center;gap:5px}
.brand-mark{width:9px;height:9px;background:var(--ink)}
.nav{position:absolute;left:306px;top:22px;display:flex;gap:13px;font-size:8.4px;font-weight:500;color:var(--ink)}

.rule{position:absolute;left:61px;width:585px;height:1px;background:var(--accent-line)}
.centered{position:absolute;left:0;width:703px;text-align:center;color:var(--white)}
.hero-kicker{top:91px;font-size:15px;font-weight:400}
.hero-title{top:113px;font-size:21px;font-weight:300}
.hero-tag{top:142px;font-size:14px;font-weight:500;letter-spacing:.2px}
.body-copy{position:absolute;left:80px;width:545px;font-size:8.5px;line-height:12.5px;text-align:center;color:var(--white);font-weight:400}
.hero .body-copy{top:180px}

.about-title{top:150px;font-size:22px;font-weight:300}
.about .body-copy{top:196px}
.btn{position:absolute;height:16px;background:var(--accent);color:var(--white);font-size:8.4px;display:flex;align-items:center;justify-content:center;border-radius:4px}
.about .btn{left:278px;top:270px;width:146px}

.contact-photo{position:absolute;left:62px;top:53px;width:282px;height:220px;border:1px solid #9a9a9a;background:
  radial-gradient(ellipse at 55% 50%,#f0a640 0%,rgba(240,166,64,0) 40%),
  linear-gradient(180deg,#d9a06c 0%,#b98256 20%,#5e3f28 45%,#7a5a3c 62%,#3e4d1f 76%,#2f3d17 100%)}
.form-panel{position:absolute;left:358px;top:51px;width:283px;height:300px;background:var(--panel);border-top:3px solid rgba(150,150,150,.7);border-radius:3px}
.form-title{position:absolute;left:0;width:283px;top:32px;text-align:center;color:var(--white);font-size:17px;font-weight:500}
.field-label{position:absolute;left:26px;color:var(--white);font-size:8.5px;font-weight:600}
.field-input{position:absolute;left:26px;width:231px;height:16px;border-bottom:1px solid #e6e6e6;color:#bdbdbd;font-size:8.5px;padding-top:2px}
.field-area{position:absolute;left:26px;top:164px;width:231px;height:44px;background:rgba(255,255,255,.85);border-radius:3px}
.form-panel .btn{left:26px;top:225px;width:151px}

.footer{position:absolute;left:0;top:1050px;width:703px;height:121px;background:linear-gradient(180deg,var(--footer-top) 0%,var(--footer-bottom) 100%);border-top:2px solid #f0e0d0;color:var(--white)}
.footer-brand{position:absolute;left:148px;top:40px;font-size:12px;font-weight:500;display:flex;align-items:center;gap:5px}
.footer-brand .brand-mark{background:var(--white)}
.footer-col{position:absolute;top:13px;font-size:5.6px;line-height:9.5px;font-weight:300}
.footer-col h4{font-size:6.4px;font-weight:500;margin-bottom:5px}
.col-address{left:324px}
.col-address h4{margin-left:50px}
.contact-line{display:flex;align-items:center;gap:3px}
.col-menu{left:472px}
.col-menu h4{margin-left:18px}
.social{position:absolute;left:580px;top:30px;display:flex;gap:5px}
.social span{width:8px;height:8px;border-radius:50%;background:var(--white)}
.copyright{position:absolute;left:0;width:703px;top:75px;text-align:center;font-size:6px;font-weight:500}
</style>
</head>
<body>
<div class="site">

  <section class="section hero">
    <div class="photo photo-front" role="img" aria-label="Stone and timber custom home at sunset, front view"></div>
    <header class="header">
      <div class="brand"><span class="brand-mark"></span>WADE HOLLORAN</div>
      <nav class="nav"><span>Home</span><span>About Us</span><span>Contact Us</span></nav>
    </header>
    <p class="centered hero-kicker">Building beautiful custom homes</p>
    <h1 class="centered hero-title">in Indianapolis for over 20 years</h1>
    <p class="centered hero-tag">GUARANTEED CONSISTENCY &amp; DEDICATION.</p>
    <div class="rule" style="top:172px"></div>
    <p class="body-copy">Lorem ipsum dolor sit amet, consectetur adipiscing elit. Sed a lacus dolor. Vestibulum ante ipsum primis in faucibus orci luctus et ultrices posuere cubilia curae; Ut leo neque, ullamcorper sed nisi non, finibus imperdiet diam. Proin interdum vulputate velit. Proin interdum in nisi vel consectetur. Suspendisse placerat, mi ornare cursus semper, est risus vestibulum leo, eu condimentum nunc quam at dui. Curabitur posuere ut ante id vehicula. Morbi at luctus purus. Praesent venenatis neque ac gravida consequat. Integer nibh purus, porttitor at aliquam eget, fringilla sit amet lacus. Pellentesque mattis ultrices eleifend. Aenean feugiat, arcu ac facilisis interdum, lacus mauris dignissim est, nec vestibulum orci nisl eget nibh. Sed auctor tortor quis ligula rutrum, vitae iaculis massa fermentum. Vestibulum eget ipsum posuere, rutrum nulla a, faucibus libero. Aliquam erat volutpat. Etiam eleifend ex lectus</p>
    <div class="rule" style="top:286px"></div>
  </section>

  <section class="section about">
    <div class="photo photo-back" role="img" aria-label="Rear of custom home at dusk with patio, fire pit and pool"></div>
    <header class="header">
      <div class="brand"><span class="brand-mark"></span>WADE HOLLORAN</div>
      <nav class="nav"><span>Home</span><span>About Us</span><span>Contact Us</span></nav>
    </header>
    <h2 class="centered about-title">Building beautiful custom homes</h2>
    <div class="rule" style="top:187px"></div>
    <p class="body-copy">Wade Holloran has been building stunning custom homes in the Indianpolis area for over 20 years. As a small boutique building company we only build a handful of homes a year in order to offer our clients the personal attention that their homes deserve. It's this attention to detail that makes our client experience and final product something special and unique.</p>
    <div class="rule" style="top:250px"></div>
    <div class="btn">Contact Us</div>
  </section>

  <section class="section contact">
    <div class="photo photo-contact" role="img" aria-label="Faded front view of custom home at sunset"></div>
    <header class="header">
      <div class="brand"><span class="brand-mark"></span>WADE HOLLORAN</div>
      <nav class="nav"><span>Home</span><span>About Us</span><span>Contact Us</span></nav>
    </header>
    <div class="contact-photo" role="img" aria-label="Custom home rear patio and lawn at dusk"></div>
    <form class="form-panel">
      <h2 class="form-title">Contact Us</h2>
      <div class="field-label" style="top:68px">Name:</div>
      <div class="field-input" style="top:81px">Enter Name</div>
      <div class="field-label" style="top:112px">Phone:</div>
      <div class="field-input" style="top:125px">Enter phone</div>
      <div class="field-label" style="top:151px">Message:</div>
      <div class="field-area"></div>
      <div class="btn">Send message</div>
    </form>
  </section>

  <footer class="footer">
    <div class="footer-brand"><span class="brand-mark"></span>WADE HOLLORAN</div>
    <div class="footer-col col-address">
      <h4>Address</h4>
      <div class="contact-line">
        <svg width="6" height="6" viewBox="0 0 24 24"><path fill="#fff" d="M6.6 10.8a15 15 0 006.6 6.6l2.2-2.2a1 1 0 011-.25 11.4 11.4 0 003.6.57 1 1 0 011 1V20a1 1 0 01-1 1A17 17 0 013 4a1 1 0 011-1h3.5a1 1 0 011 1c0 1.25.2 2.45.57 3.6a1 1 0 01-.25 1z"/></svg>
        317-552-7190</div>
      <div class="contact-line">
        <svg width="6" height="6" viewBox="0 0 24 24"><path fill="#fff" d="M2 5h20v14H2z"/><path fill="none" stroke="#8a3e1c" stroke-width="2" d="M2 5l10 8 10-8"/></svg>
        wade@whcrafted.com</div>
      <div>415 North Fernmill Rd, Suite 308,</div>
      <div>Carmel IN 46033</div>
    </div>
    <div class="footer-col col-menu">
      <h4>Menu</h4>
      <div>Home</div>
      <div>About Us</div>
      <div>Contact Us</div>
    </div>
    <div class="social"><span></span><span></span><span></span></div>
    <p class="copyright">WADE HOLLORAN | 2023 | All Rights Reserved</p>
  </footer>

</div>
</body>
</html>
```